Social Media Card

We would like a social media card to hand out to our customers.
It should be double sided, with the front to say in bold letters Follow Us!
We would like the card to be two toned in our brand colors (espresso brown & copper.) I still want a modern, clean look to the card but it can be a bit more "fun" than our business cards. I have attached the previous card that you did but you don't have to stick to the brown background/copper lettering as shown.
The font is josefin. We would need our logo either on the front or the back side.
I think I want social media icons but not the same old boring ones.
Our social media information is as follows:
Facebook: Valmonte Jewelry
Twitter: Valmonte Jewelry
Pinterest: vmkqpw
Instagram: Valmonte Jewelry
Looking forward to seeing what you come up with!
Thanks!
Gwen

Our address, etc info will need to be added.

Brisbury Lane # 7

Stonegate Plaza

Londonderry, NH 03981

(603)519-8074

www.valmontejewelry.example

info@valmontejewelry.example

```html
<!DOCTYPE html>
<html lang="en">
<head>
<meta charset="utf-8">
<title>Valmonte Jewelry – Social Media Card</title>
<link rel="stylesheet" href="https://fonts.googleapis.com/css2?family=Josefin+Sans:wght@300;400;600&family=Source+Sans+3:wght@400&display=swap">
<style>
  :root {
    --espresso: #200d0b;
    --copper: #c36d33;
    --cream: #ffffff;
    --page: #ffffff;
    --label: #1a1a1a;
  }
  * { margin: 0; padding: 0; box-sizing: border-box; }
  html, body {
    width: 912px;
    height: 1200px;
    overflow: hidden;
    background: var(--page);
  }
  .sheet {
    position: relative;
    width: 912px;
    height: 1200px;
    font-family: "Josefin Sans", sans-serif;
  }
  .card {
    position: absolute;
    width: 851px;
    height: 497px;
    background: var(--espresso);
    overflow: hidden;
  }
  .card--front { left: 33px; top: 35px; }
  .card--back  { left: 30px; top: 617px; }
  .card svg { position: absolute; inset: 0; display: block; }
  .band { fill: var(--copper); }
  .headline {
    fill: var(--cream);
    font-family: "Josefin Sans", sans-serif;
    font-weight: 400;
    font-size: 94px;
    letter-spacing: 3px;
  }
  .brand-name, .brand-tagline {
    fill: var(--cream);
    font-family: "Josefin Sans", sans-serif;
  }
  .brand-name { font-size: 78px; font-weight: 600; letter-spacing: 1px; }
  .brand-tagline { font-size: 30px; font-weight: 400; }
  .side-label {
    position: absolute;
    left: 0;
    width: 936px;
    text-align: center;
    font-family: "Source Sans 3", sans-serif;
    font-size: 32px;
    color: var(--label);
    letter-spacing: 0.5px;
  }
  .side-label--front { top: 562px; }
  .side-label--back  { top: 1150px; }
  .profile {
    position: absolute;
    display: flex;
    align-items: center;
    gap: 14px;
    color: var(--copper);
    font-family: "Josefin Sans", sans-serif;
    font-weight: 300;
    font-size: 29px;
    line-height: 1;
  }
  .profile__dot {
    width: 32px;
    height: 32px;
    border-radius: 50%;
    background: var(--copper);
    flex: none;
  }
  .profile--top-left     { left: 56px;  top: 358px; }
  .profile--top-right    { left: 349px; top: 356px; }
  .profile--bottom-left  { left: 92px;  top: 420px; }
  .profile--bottom-right { left: 270px; top: 420px; }
</style>
</head>
<body>
<main class="sheet">
  <section class="card card--front" aria-label="Card front">
    <svg width="851" height="497" viewBox="0 0 851 497">
      <polygon class="band" points="400,0 622,0 125,497 0,497 0,402"/>
      <text class="headline" text-anchor="middle" dominant-baseline="middle"
            transform="translate(266,252) rotate(-45)">Follow Us!</text>
    </svg>
  </section>
  <p class="side-label side-label--front">FRONT</p>

  <section class="card card--back" aria-label="Card back">
    <svg width="851" height="497" viewBox="0 0 851 497">
      <polygon class="band" points="402,0 622,0 851,229 851,449"/>
      <text class="brand-name" text-anchor="middle" dominant-baseline="middle"
            transform="translate(690,160) rotate(45)">valmonte</text>
      <text class="brand-tagline" text-anchor="middle" dominant-baseline="middle"
            transform="translate(646,200) rotate(45)">Jewelry &amp; Design Studio</text>
    </svg>
    <div class="profile profile--top-left"><span class="profile__dot"></span><span>Valmonte Jewelry</span></div>
    <div class="profile profile--top-right"><span class="profile__dot"></span><span>Valmonte Jewelry</span></div>
    <div class="profile profile--bottom-left"><span class="profile__dot"></span><span>vmkqpw</span></div>
    <div class="profile profile--bottom-right"><span class="profile__dot"></span><span>Valmonte Jewelry</span></div>
  </section>
  <p class="side-label side-label--back">BACK</p>
</main>
</body>
</html>
```